Business card design for Birch Engineering Torvant

We need a new business card design along with all the necessary to place an order. The company is Birch Engineering Torvant and we recently updated our logo.

```html
<!DOCTYPE html>
<html lang="en">
<head>
<meta charset="utf-8">
<title>Birch Engineering Torvant – Business Card</title>
<link rel="stylesheet" href="https://fonts.googleapis.com/css2?family=Montserrat:wght@700;800&family=Nunito+Sans:wght@400;600&display=swap">
<style>
  :root {
    --stage: #3a3a3c;
    --card: #1f1f20;
    --card-edge: #2a2a2b;
    --ink-grey: #9b9b9d;
    --ink-light: #b9b9bb;
    --accent: #e9c21d;
    --strip: #7a7a7c;
  }
  * { box-sizing: border-box; margin: 0; padding: 0; }
  html, body {
    width: 1200px; height: 982px; overflow: hidden;
    background: var(--stage);
  }
  .canvas { position: relative; width: 1200px; height: 982px; }
  .card {
    position: absolute;
    width: 700px; height: 400px;
    background: var(--card);
    border-radius: 26px;
    box-shadow: 0 18px 40px rgba(0,0,0,.45);
    overflow: hidden;
  }
  .card--front { left: 400px; top: 70px; }
  .card--back { left: 100px; top: 510px; }

  .brand {
    font-family: "Montserrat", sans-serif;
    font-weight: 800;
    color: var(--ink-grey);
    display: flex; align-items: center; gap: 14px;
    line-height: 1.05;
    text-transform: uppercase;
    letter-spacing: .04em;
  }
  .brand__mark { background: var(--accent); flex: none; }
  .card--front .brand {
    position: absolute; left: 0; right: 0; top: 0; bottom: 0;
    justify-content: center; font-size: 38px; color: #4a4a4c;
  }
  .card--front .brand__mark { width: 26px; height: 26px; }

  .card--back .edge-strip {
    position: absolute; left: 0; top: 70px; width: 10px; height: 220px;
    background: var(--strip);
  }
  .card--back .brand {
    position: absolute; left: 70px; top: 50px; font-size: 24px;
  }
  .card--back .brand__mark { width: 18px; height: 18px; }

  .contact {
    position: absolute; left: 70px; top: 150px;
    list-style: none;
    font-family: "Nunito Sans", sans-serif;
    font-size: 17px; color: var(--ink-light);
  }
  .contact li { display: flex; align-items: flex-start; gap: 12px; margin-bottom: 8px; line-height: 1.35; }
  .contact svg { width: 16px; height: 16px; flex: none; margin-top: 3px; fill: var(--accent); }

  .person {
    position: absolute; right: 60px; top: 150px; text-align: right;
  }
  .person__name {
    font-family: "Montserrat", sans-serif; font-weight: 800;
    font-size: 32px; color: var(--ink-grey); letter-spacing: .01em;
  }
  .person__role {
    font-family: "Nunito Sans", sans-serif; font-weight: 400;
    font-size: 19px; color: var(--accent); margin-top: 4px;
  }
</style>
</head>
<body>
<main class="canvas">
  <section class="card card--front" aria-label="Card front">
    <div class="brand"><span class="brand__mark"></span><span>Birch Engineering Torvant</span></div>
  </section>

  <section class="card card--back" aria-label="Card back">
    <div class="edge-strip"></div>
    <div class="brand"><span class="brand__mark"></span><span>Birch Engineering<br>Torvant</span></div>

    <ul class="contact">
      <li>
        <svg viewBox="0 0 16 16"><path d="M8 0a5.5 5.5 0 0 0-5.5 5.5C2.5 10 8 16 8 16s5.5-6 5.5-10.5A5.5 5.5 0 0 0 8 0zm0 8a2.5 2.5 0 1 1 0-5 2.5 2.5 0 0 1 0 5z"/></svg>
        <span>423 Street Address Here, City<br>State, Country, ZIP Code</span>
      </li>
      <li>
        <svg viewBox="0 0 16 16"><path d="M3.5 1l2.5 3-1.5 2c1 2 3 4 5 5l2-1.5 3 2.5-1.5 2.5C8 15 1 8 1 2.5z"/></svg>
        <span>(123) 456-7890</span>
      </li>
      <li>
        <svg viewBox="0 0 16 16"><path d="M4 0h8a1 1 0 0 1 1 1v14a1 1 0 0 1-1 1H4a1 1 0 0 1-1-1V1a1 1 0 0 1 1-1zm1 2v10h6V2zm3 11a1 1 0 1 0 0 2 1 1 0 0 0 0-2z"/></svg>
        <span>(123) 456-7890</span>
      </li>
      <li>
        <svg viewBox="0 0 16 16"><path d="M4 0h8v4H4zM1 5h14v7h-3v4H4v-4H1zm4 5v4h6v-4z"/></svg>
        <span>(123) 456-7890</span>
      </li>
      <li>
        <svg viewBox="0 0 16 16"><path d="M0 3h16v1.2L8 9 0 4.2zm0 2.6 8 4.8 8-4.8V13H0z"/></svg>
        <span>info@yourwebsitehere.com</span>
      </li>
      <li>
        <svg viewBox="0 0 16 16"><circle cx="8" cy="8" r="7.5"/><path d="M1 8h14M8 .5c-3 3.5-3 11.5 0 15M8 .5c3 3.5 3 11.5 0 15" stroke="#1f1f20" stroke-width="1" fill="none"/></svg>
        <span>yourwebsitehere.com</span>
      </li>
    </ul>

    <div class="person">
      <div class="person__name">DANIEL REYES</div>
      <div class="person__role">Founder &amp; CEO</div>
    </div>
  </section>
</main>
</body>
</html>
```